Flu Vaccination Poster

I would like a banner designed to display from the ceiling in my pharmacy promoting flu vaccination.
In large words, it should say "Flu Vaccination"
In smaller text it should say "Available here. See in store for details"
It should also display our website kestrelvalepharmacy.com.au and have a message for more information visit the website.
Currently patients required to pay for the service, however in May this year the vaccine will become free for everyone, so I would like to put a sticker on the sign in May saying "FREE" and then remove the sticker when no longer free. The banner dimensions are "2.19m wide x 0.61m tall.
I have uploaded logo files plus a photo of a previously used banner which is no longer relevant. More formats of logo files are available if required.

```html
<!DOCTYPE html>
<html lang="en">
<head>
<meta charset="utf-8">
<title>Flu Vaccination Banner</title>
<link rel="stylesheet" href="https://fonts.googleapis.com/css2?family=Poppins:wght@400;500;600;700;800&family=Fira+Sans+Extra+Condensed:wght@800&display=swap">
<style>
  :root {
    --pink: #d61a63;
    --navy: #253a63;
    --blue: #3399c4;
    --orange: #ffab00;
    --ink: #1f2540;
    --grey: #4a4a52;
    --white: #ffffff;
    --page: #ffffff;
  }
  * { margin: 0; padding: 0; box-sizing: border-box; }
  html, body {
    width: 1200px;
    height: 600px;
    overflow: hidden;
    background: var(--page);
    font-family: "Poppins", sans-serif;
  }
  .banner {
    position: absolute;
    left: 110px;
    top: 163px;
    width: 980px;
    height: 273px;
    background: var(--white);
    overflow: hidden;
  }
  .headline-band {
    position: absolute;
    left: 0;
    top: 0;
    width: 980px;
    height: 155px;
    background: var(--navy);
  }
  .headline-band .flag {
    position: absolute;
    left: 0;
    top: 0;
  }
  .headline {
    position: absolute;
    top: 18px;
    font-family: "Poppins", sans-serif;
    font-weight: 700;
    color: var(--white);
    line-height: 1;
    white-space: nowrap;
  }
  .headline--flu {
    left: 38px;
    font-size: 108px;
    letter-spacing: -2px;
  }
  .headline--vaccination {
    left: 274px;
    font-size: 110px;
    letter-spacing: -2px;
  }
  .pill {
    position: absolute;
    top: 140px;
    height: 31px;
    border-radius: 16px;
    color: var(--white);
    font-weight: 700;
    font-size: 17px;
    line-height: 31px;
    text-align: center;
    white-space: nowrap;
  }
  .pill--available { left: 502px; width: 169px; background: var(--pink); }
  .pill--details { left: 691px; width: 247px; background: var(--blue); }
  .free-sticker {
    position: absolute;
    left: 36px;
    top: 181px;
    width: 148px;
    height: 58px;
    background: var(--orange);
    border-radius: 56px 0 0 0;
    color: var(--white);
    font-family: "Fira Sans Extra Condensed", sans-serif;
    font-weight: 800;
    font-size: 44px;
    line-height: 58px;
    text-align: right;
    padding-right: 16px;
    letter-spacing: 1px;
  }
  .info {
    position: absolute;
    left: 308px;
    top: 186px;
    white-space: nowrap;
  }
  .info__lead {
    font-size: 15.5px;
    font-weight: 400;
    color: var(--grey);
    line-height: 1;
  }
  .info__url {
    margin-top: 8px;
    font-size: 23px;
    font-weight: 600;
    color: var(--ink);
    line-height: 1;
  }
  .brand {
    position: absolute;
    left: 772px;
    top: 190px;
    display: flex;
    align-items: center;
    gap: 8px;
  }
  .brand__dot {
    width: 20px;
    height: 20px;
    border-radius: 50%;
    background: var(--pink);
  }
  .brand__name {
    font-weight: 600;
    font-size: 20px;
    line-height: 1.05;
    color: var(--navy);
  }
</style>
</head>
<body>
  <div class="banner">
    <div class="headline-band">
      <svg class="flag" width="280" height="155" viewBox="0 0 280 155" aria-hidden="true">
        <polygon points="0,0 232,0 276,155 0,155" fill="var(--pink)"/>
      </svg>
      <span class="headline headline--flu">FLU</span>
      <span class="headline headline--vaccination">Vaccination</span>
    </div>
    <div class="pill pill--available">Available here</div>
    <div class="pill pill--details">See in store for details</div>
    <div class="free-sticker">FREE</div>
    <div class="info">
      <p class="info__lead">For more information visit the website.</p>
      <p class="info__url">kestrelvalepharmacy.com.au</p>
    </div>
    <div class="brand">
      <span class="brand__dot"></span>
      <span class="brand__name">kestrel vale<br>pharmacy</span>
    </div>
  </div>
</body>
</html>
```